Quorlan Visit cards serious but not sad

Hello, I'd like to design my visit cards with the logo Quorlan (attached) the following information: Name: Mathis Deloraux Title: Mobile Director: 33 (0) 6 28 40 13 85 Phone: 33 (0) 4 71 86 52 09 e-mail: mathis.deloraux@quorlan-advisory.example address: 17 Rue Anatole Berrin 92400 Courbevoie This visit will be used on the banking institutions and Quorlan is a consulting firm. I do not want to have dark background.

Target Market(s)

banks

Contact Information for Business Card

Name : Mathis Deloraux
Title : Director
mobile : +33(0)6 28 40 13 85
Phone : +33(0)4 71 86 52 09
e-mail: mathis.deloraux@quorlan-advisory.example
adresse : 17 Rue anatole Berrin 92310 Valmerange

Requirements
Nice to have
• serious but not sad

```html
<!DOCTYPE html>
<html lang="en">
<head>
<meta charset="utf-8">
<title>Quorlan business card</title>
<link rel="stylesheet" href="https://fonts.googleapis.com/css2?family=Exo+2:wght@500;700&family=Cabin:wght@400&display=swap">
<style>
  :root {
    --brand-blue: #1477c2;
    --brand-blue-deep: #1170b8;
    --card-white: #f7f7f7;
    --ink: #2b2b2b;
    --stage: #666666;
    --faint-grey: #e4e4e4;
  }
  * { margin: 0; padding: 0; box-sizing: border-box; }
  html, body { width: 1200px; height: 802px; overflow: hidden; }
  body { background: var(--stage); position: relative; font-family: "Cabin", sans-serif; }

  .card { position: absolute; top: 274px; width: 443px; height: 265px; overflow: hidden; }
  .card--front { left: 136px; background: var(--card-white); }
  .card--back { left: 624px; background: var(--brand-blue); }

  .front-disc {
    position: absolute; left: 291px; top: 22px; width: 202px; height: 202px; border-radius: 50%;
    background: radial-gradient(circle at 35% 40%, #f2f2f2 0%, var(--faint-grey) 55%, #d9d9d9 100%);
  }

  .brand { position: absolute; left: 24px; top: 24px; display: flex; align-items: center; gap: 10px; }
  .brand__dot { width: 77px; height: 77px; border-radius: 50%; background: var(--brand-blue); }
  .brand__name { font-family: "Exo 2", sans-serif; font-weight: 500; font-size: 44px; color: var(--brand-blue); letter-spacing: 0.5px; }

  .person { position: absolute; left: 24px; top: 120px; }
  .person__name { font-family: "Exo 2", sans-serif; font-weight: 700; font-size: 15px; color: var(--brand-blue); letter-spacing: 0.3px; line-height: 1.1; }
  .person__title { font-size: 13px; color: var(--ink); line-height: 1.2; }

  .contact { position: absolute; left: 24px; top: 164px; list-style: none; font-size: 13px; color: var(--ink); }
  .contact li { display: flex; align-items: center; gap: 3px; height: 15.5px; white-space: nowrap; }
  .contact li.contact__address { margin-top: 9px; }
  .contact svg { width: 10px; height: 10px; fill: var(--brand-blue); flex: none; }

  .back-pattern { position: absolute; inset: 0; background: var(--brand-blue-deep); }
  .back-brand {
    position: absolute; left: 262px; top: 168px; width: 116px; text-align: center;
    font-family: "Exo 2", sans-serif; font-weight: 500; font-size: 20px; color: #ffffff;
  }
</style>
</head>
<body>
  <section class="card card--front">
    <div class="front-disc"></div>
    <div class="brand">
      <span class="brand__dot"></span>
      <span class="brand__name">Quorlan</span>
    </div>
    <div class="person">
      <p class="person__name">MATHIS DELORAUX</p>
      <p class="person__title">Director</p>
    </div>
    <ul class="contact">
      <li><svg viewBox="0 0 10 10"><path d="M2.5 0h5a1 1 0 0 1 1 1v8a1 1 0 0 1-1 1h-5a1 1 0 0 1-1-1V1a1 1 0 0 1 1-1zm0.3 1.2v6.6h4.4V1.2zM5 8.3a.5.5 0 1 0 0 1 .5.5 0 0 0 0-1z"/></svg>+33(0)6 28 40 13 85</li>
      <li><svg viewBox="0 0 10 10"><path d="M0 3.5C1 1.5 9 1.5 10 3.5L9 5 7 4.3V3.4C6 3 4 3 3 3.4v.9L1 5zM2 5.2 3.5 4.5h3L8 5.2V9H2zm3 .8a1.3 1.3 0 1 0 0 2.6A1.3 1.3 0 0 0 5 6z"/></svg>+33(0)4 71 86 52 09</li>
      <li><svg viewBox="0 0 10 10"><path d="M0 2h10v6H0zm1 .8v.3l4 2.5 4-2.5v-.3zM1 4.2V7.2h8V4.2L5 6.7z"/></svg>mathis.deloraux@quorlan-advisory.example</li>
      <li class="contact__address"><svg viewBox="0 0 10 10"><path d="M5 0a3.5 3.5 0 0 1 3.5 3.5C8.5 6 5 10 5 10S1.5 6 1.5 3.5A3.5 3.5 0 0 1 5 0zm0 2a1.5 1.5 0 1 0 0 3 1.5 1.5 0 0 0 0-3z"/></svg>17 Rue anatole Berrin 92310 Valmerange</li>
    </ul>
  </section>

  <section class="card card--back">
    <div class="back-pattern" role="img" aria-label="Repeating brand pattern in soft blue tones"></div>
    <p class="back-brand">Quorlan</p>
  </section>
</body>
</html>
```